Financing company needs a 1-page website with contact form

We are a financing company focusing on manufacturing sector. We need a simple 1 page website with contact form that is consistent and aligned to the main website (it is part of a bigger company). Please adhere to the same color scheme to make it look similar, but not necessarily a carbon copy.

Website link www.orvik-holdings.net

I also need the designer to suggest stock images that are suitable (related to manufacturing sector).

Files to be in html format.

Font: Try to match the main website or use a simple, sans serif font that is similar
Updates

Project Deadline Extended
Reason: Dear designers, thank you for your submissions. I believe I have given my feedback to all of you. But we would like to extend it by a few days to give a chance for more designers to join, and tweak the existing submissions. Thanks!

Target Market(s)

Small and medium companies in manufacturing sector, potential investors

Industry/Entity Type

Financial Service

Font styles to use
Sans Serif

Requirements
Must have
• Consistency to the main website www.orvik-holdings.net
• Can use simialr layout too to make it easier
• Contact form
• to have a one page website like this example https://www.trymolbe.com/

```html
<!DOCTYPE html>
<html lang="en">
<head>
<meta charset="utf-8">
<title>Halden Ridge Factoring</title>
<link rel="stylesheet" href="https://fonts.googleapis.com/css2?family=Archivo+Narrow:wght@400&display=swap">
<style>
  :root {
    --ink: #1a1a1a;
    --ink-soft: #2b2b2b;
    --white: #ffffff;
    --rule: #bdbdbd;
    --brand-red: #c8323c;
    --band-red: #780a10;
    --band-red-light: #8a1a18;
    --panel: #f3f3f3;
    --night-deep: #04080c;
    --night: #0d1822;
    --night-haze: #202a2a;
    --night-lit: #343629;
    --footer-line: #1c1c1c;
  }
  * { box-sizing: border-box; margin: 0; padding: 0; }
  html, body {
    width: 1200px;
    height: 1000px;
    overflow: hidden;
    background: var(--white);
    font-family: "Archivo Narrow", "Arial Narrow", sans-serif;
    color: var(--ink);
  }
  .page { position: relative; width: 1200px; height: 1000px; overflow: hidden; }

  .site-header {
    position: absolute; top: 0; left: 0; width: 1200px; height: 67px;
    border-top: 3px solid var(--rule);
    background: var(--white);
  }
  .brand {
    position: absolute; left: 350px; top: 17px;
    display: flex; align-items: center; gap: 8px;
  }
  .brand-mark { width: 20px; height: 20px; background: var(--brand-red); }
  .brand-name {
    font-size: 29px; line-height: 30px; color: var(--ink-soft);
  }
  .main-nav {
    position: absolute; left: 633px; top: 23px;
    display: flex; gap: 13px; font-size: 15.5px; color: var(--ink);
  }

  .hero {
    position: absolute; top: 67px; left: 0; width: 1200px; height: 423px;
    background: linear-gradient(100deg, var(--night-deep) 0%, var(--night) 38%, var(--night-haze) 70%, var(--night-lit) 100%);
  }
  .hero-band {
    position: absolute; left: 0; top: 490px; width: 1200px; height: 102px;
    background: linear-gradient(90deg, var(--band-red) 0%, #7f0c12 60%, var(--band-red-light) 100%);
  }
  .hero-tagline {
    position: absolute; left: 343px; top: 36px;
    font-size: 23px; font-weight: 400; color: var(--white);
  }

  .section { position: absolute; left: 338px; width: 500px; }
  .section-label {
    display: inline-block; width: 96px; height: 20px;
    background: var(--brand-red); color: var(--white);
    font-size: 13px; line-height: 20px; text-align: center;
  }
  .section-body {
    margin-top: 4px; background: var(--panel);
    box-shadow: 0 1px 4px rgba(0,0,0,0.3);
    padding: 1px 5px 14px;
    font-size: 13px; line-height: 17.5px; color: var(--ink);
  }
  .section-body p + p { margin-top: 17.5px; }
  .about { top: 660px; }
  .services { top: 878px; }

  .page-edge {
    position: absolute; left: 0; bottom: 0; width: 1200px; height: 4px;
    background: var(--footer-line);
  }
</style>
</head>
<body>
<div class="page">
  <header class="site-header">
    <div class="brand">
      <span class="brand-mark"></span>
      <span class="brand-name">HALDEN RIDGE</span>
    </div>
    <nav class="main-nav">
      <span>About</span><span>Services</span><span>Personnel</span><span>Contact</span>
    </nav>
  </header>

  <div class="hero" role="img" aria-label="Photograph: night view of Earth from space with the lit cities of Europe"></div>
  <div class="hero-band">
    <h1 class="hero-tagline">Nurturing Partnerships to Drive Real Economic Growth</h1>
  </div>

  <section class="section about">
    <span class="section-label">Who are we?</span>
    <div class="section-body">
      <p>Halden Ridge Factoring is a specialist financier focusing on small and medium-sized enterprises (SMEs) in emerging markets. We provide working capital, typically in structured trade finance, to businesses in the manufacturing and retail sectors.</p>
      <p>We are supported by a team of highly experienced professionals with in-depth knowledge of credit, private equity and investments.</p>
    </div>
  </section>

  <section class="section services">
    <span class="section-label">Our Services</span>
    <div class="section-body">
      <p>Our key focus is on companies in the manufacturing sector that are in need of working capital. We meet their financing needs by developing structured offerings after a careful analysis of the companies' operations and processes. Our business model is based on structured lending in the form of trade finance facilities. How we are different is the way we combine a best practices mezzanine discipline with our experience in trade finance structuring.</p>
    </div>
  </section>

  <div class="page-edge"></div>
</div>
</body>
</html>
```